Rio Calmo Lighting Distributors Business Card Design

Use logo and expand the framing box to the extents of the business card. Keep company name in right bottom corner and triangle at top right corner. I would like to have a template so that I can fill in employee name, contact info, email and website.

```html
<!DOCTYPE html>
<html lang="en">
<head>
<meta charset="utf-8">
<title>Rio Calmo Lighting Distributors – Business Card</title>
<link href="https://fonts.googleapis.com/css2?family=Montserrat:wght@400;700;800&display=swap" rel="stylesheet">
<style>
  :root {
    --backdrop: #dcdbd8;
    --card-white: #ffffff;
    --card-black: #000000;
    --brand-blue: #0784c9;
    --ink: #111111;
    --ink-soft: #333333;
  }
  html, body {
    margin: 0;
    width: 1200px;
    height: 801px;
    overflow: hidden;
    background: var(--backdrop);
    font-family: "Montserrat", sans-serif;
  }
  .stage {
    position: relative;
    width: 1200px;
    height: 801px;
  }
  .card {
    position: absolute;
    top: 252px;
    width: 520px;
    height: 297px;
    border-radius: 18px;
    overflow: hidden;
    box-shadow: 0 0 0 3px var(--brand-blue), 0 14px 30px rgba(0,0,0,0.18);
  }
  .card--front { left: 60px; background: var(--card-white); }
  .card--back  { left: 620px; background: var(--card-black); }

  .front-wave {
    position: absolute;
    inset: 0;
    width: 100%;
    height: 100%;
  }
  .wordmark {
    position: absolute;
    font-weight: 800;
    text-transform: uppercase;
    line-height: 1.02;
    letter-spacing: 0.5px;
  }
  .card--front .wordmark {
    left: 34px;
    top: 104px;
    width: 200px;
    font-size: 25px;
    color: var(--ink);
  }
  .card--back .wordmark {
    right: 46px;
    bottom: 44px;
    font-size: 36px;
    color: #ffffff;
    text-align: left;
  }
  .divider {
    position: absolute;
    left: 248px;
    top: 58px;
    width: 1.5px;
    height: 180px;
    background: var(--brand-blue);
  }
  .contact {
    position: absolute;
    left: 266px;
    top: 52px;
    color: var(--ink-soft);
  }
  .contact__name {
    margin: 0;
    font-size: 22px;
    font-weight: 800;
    color: var(--brand-blue);
  }
  .contact__role {
    margin: 2px 0 20px;
    font-size: 12px;
  }
  .contact__list {
    list-style: none;
    margin: 0 0 18px;
    padding: 0;
    font-size: 12px;
  }
  .contact__list li {
    display: flex;
    align-items: center;
    gap: 7px;
    margin-bottom: 3px;
  }
  .contact__list svg { width: 11px; height: 11px; fill: var(--brand-blue); }
  .contact__address {
    margin: 0;
    font-size: 12px;
    line-height: 1.35;
    font-style: normal;
  }
</style>
</head>
<body>
<main class="stage">

  <section class="card card--front" aria-label="Card front">
    <svg class="front-wave" viewBox="0 0 520 297" preserveAspectRatio="none" aria-hidden="true">
      <path d="M520 0 L500 0 C470 120 430 220 330 297 L520 297 Z" fill="var(--card-black)"/>
      <path d="M520 0 L506 0 C480 120 444 224 346 297 L520 297 Z" fill="var(--card-white)"/>
      <path d="M520 0 L512 0 C488 124 454 226 360 297 L520 297 Z" fill="var(--brand-blue)"/>
    </svg>

    <div class="wordmark">Rio Calmo<br>Lighting<br>Distributors</div>

    <div class="divider"></div>

    <div class="contact">
      <h1 class="contact__name">Daniel Moreno</h1>
      <p class="contact__role">Managing Director</p>
      <ul class="contact__list">
        <li>
          <svg viewBox="0 0 24 24" aria-hidden="true"><path d="M6.6 10.8a15 15 0 0 0 6.6 6.6l2.2-2.2c.3-.3.7-.4 1-.2 1.1.4 2.3.6 3.6.6.6 0 1 .4 1 1V20c0 .6-.4 1-1 1A17 17 0 0 1 3 4c0-.6.4-1 1-1h3.5c.6 0 1 .4 1 1 0 1.3.2 2.5.6 3.6.1.3 0 .7-.2 1z"/></svg>
          123 456 789
        </li>
        <li>
          <svg viewBox="0 0 24 24" aria-hidden="true"><path d="M2 5h20v14H2z M2 5l10 8 10-8" stroke="#fff" stroke-width="1.5"/></svg>
          info@youremail.com
        </li>
        <li>
          <svg viewBox="0 0 24 24" aria-hidden="true"><circle cx="12" cy="12" r="10"/></svg>
          www.yourwebsite.com
        </li>
      </ul>
      <address class="contact__address">Your address, City<br>State, Zip 1234</address>
    </div>
  </section>

  <section class="card card--back" aria-label="Card back">
    <div class="wordmark">Rio Calmo<br>Lighting<br>Distributors</div>
  </section>

</main>
</body>
</html>
```